Verdant Row

Currently www.verdantrow-example.com. This site was designed with a generic templet. However it is functional. I'm looking for a fun, fresh, and professional design. I also need help getting the XML for Searchly and Findo. I'm not a web designer and need help. I do not like my current sites narrow width.
Updates

All and all I'm liking the designs. The earlier ones seem better. Some seem that they are just taking my images and inputing them into a templet. I could have done that. The pictures are nice. Please keep in mind, functionality and updates. Please help us show our customers our how we are different. Safe Reliable Responsible are the key fundamentals, inside of these fundamentals show that were are customer service specialized. We are, Licensed, Insured, Drug Screened, Criminally Screened. Seems that people are putting up nice pictures but not capturing our values. Please help us market us on our website. Show our prospective customers why we are better, how we differentiate ourself from the competitors. Why choose us? Our flyers and cards are designed to drive our prospective customers to the website. If it looks identical with no pazaz like the card, then the marketing chain failed. I included our cards to help guide the thought process of our company. The link below is a feature I would love to have. This may be another project itself. I'm not sure if PH is the place to accomplish it. Below is a link for people to estimate there lawns with globe viewer. I would like to give a range of estimates using this technology. I have no clue how to accomplish it. If anyone knows how to who could do this, Please let me know. https://www.yardquote-example.com/showOrder/MOWLAWN/propertyDetails

Target Market(s)

We target residential customers 30-80 yr old. We also are expanding and placing a special emphasis on Business accounts. The main service is a mowing and landscape maintenance. Should be the main focus of the site.

Industry/Entity Type

Searchly

Coding

Coded - Design and coding required

Font styles to use
Sans Serif

Requirements
Must have
• I want this site to be fun and colorful. It still needs to be professional looking as not to deter business accounts. If you use photos, they must reflect Florida lawn. Note the architecture the homes, grass type, types of plants.
Should not have
• My current site is ok. I use it just as a

```html
<!DOCTYPE html>
<html lang="en">
<head>
<meta charset="utf-8">
<title>Verdant Row — Lawn Care</title>
<link href="https://fonts.googleapis.com/css2?family=Raleway:wght@300;400;500;600;700&family=Montserrat:wght@400;600;700&display=swap" rel="stylesheet">
<style>
:root{
  --green:#5fa22e;
  --green-bright:#8bdc2a;
  --red:#ea4a33;
  --red-dark:#d83a24;
  --grey-text:#666;
  --heading:#555;
  --footer:#333;
  --white:#fff;
}
*{box-sizing:border-box;margin:0;padding:0}
html,body{width:880px;height:1200px;overflow:hidden;background:var(--white)}
body{position:relative;font-family:'Raleway',sans-serif;color:var(--grey-text)}
.abs{position:absolute}

/* header */
.brand{left:62px;top:30px;display:flex;align-items:center;gap:8px}
.brand-dot{width:22px;height:22px;border-radius:50%;background:var(--red)}
.brand-name{font-family:'Raleway',sans-serif;font-weight:700;font-size:28px;color:var(--green)}
.topbar{left:404px;top:0;width:412px;height:23px;background:var(--green);border-radius:0 0 6px 6px;
  color:var(--white);font-size:8.5px;letter-spacing:.4px;display:flex;align-items:center;justify-content:center;gap:8px;font-family:'Montserrat',sans-serif}
.nav{top:60px;left:400px;display:flex;gap:0}
.nav a{font-size:13px;color:#555;text-decoration:none;margin-right:44px}
.nav a.active{color:var(--red);font-weight:600}

/* hero */
.hero{left:0;top:92px;width:880px;height:298px;
  background:linear-gradient(180deg,#8fc3e8 0%,#b6d7a8 22%,#5c8d3a 55%,#3f7a25 100%)}
.hero-arrow{top:222px;width:26px;height:40px;background:rgba(255,255,255,.85);display:flex;align-items:center;justify-content:center}
.hero-arrow.left{left:0;border-radius:0 20px 20px 0}
.hero-arrow.right{right:0;border-radius:20px 0 0 20px}
.hero-band{left:0;top:320px;width:880px;height:70px;background:rgba(234,74,51,.82);text-align:center;color:var(--white)}
.hero-band h1{font-weight:400;font-size:25px;letter-spacing:.5px;margin-top:10px}
.hero-band p{font-size:14px;font-weight:300;letter-spacing:.4px}
.notch{left:412px;top:389px}

/* about */
.section-title{width:880px;left:0;text-align:center;font-weight:300;font-size:21px;color:var(--heading);letter-spacing:.5px}
.lead{left:120px;width:640px;top:447px;text-align:center;color:var(--green);font-size:14.5px;line-height:17px}
.blurb{left:70px;width:740px;top:507px;text-align:center;font-size:8.6px;line-height:11px;color:#777}

/* services */
.service{width:240px}
.service svg{position:absolute;left:0;top:0}
.service h3{position:absolute;left:65px;top:0;font-size:12px;font-weight:500;color:var(--red);white-space:nowrap}
.service p{position:absolute;left:65px;top:19px;width:165px;font-size:8.8px;line-height:12.5px;color:#888}
.service .more{position:absolute;left:65px;top:62px;font-family:'Montserrat',sans-serif;font-size:8px;font-weight:600;color:#777;letter-spacing:.3px}

/* newsletter */
.newsletter{left:0;top:800px;width:880px;height:128px}
.newsletter h2{position:absolute;left:0;width:880px;top:33px;text-align:center;color:var(--white);font-weight:500;font-size:13.5px;letter-spacing:.3px}
.field{position:absolute;top:56px;width:167px;height:33px;background:var(--white);border-radius:3px;font-size:11px;color:#777;padding:10px 0 0 14px}
.send{position:absolute;left:646px;top:56px;width:102px;height:32px;background:var(--green-bright);border-radius:3px;border-bottom:3px solid #6bb51c;
  font-family:'Montserrat',sans-serif;font-weight:700;font-size:11px;color:#2d4a12;text-align:center;padding-top:9px}

/* info */
.info h4{font-family:'Montserrat',sans-serif;font-size:14px;font-weight:600;color:#555;letter-spacing:.6px}
.info .sub{font-size:10.5px;color:#888;letter-spacing:.6px;line-height:22px}
.info .small{font-size:10px;color:#888;line-height:12px}
.info .phone{font-family:'Montserrat',sans-serif;font-weight:700;font-size:14px;color:#555;margin-top:8px}
.info .quote{font-size:15px;font-weight:300;color:#888;letter-spacing:.6px}

.grass{left:0;top:1078px;width:880px;height:60px;background:linear-gradient(180deg,#ffffff 0%,#a8d96a 45%,#5aa82a 100%)}
.mascot{left:650px;top:1024px;width:214px;height:113px;border-radius:40px 40px 10px 10px;background:linear-gradient(135deg,#e94a33,#c9d6c9)}

/* footer */
.footer{left:0;top:1137px;width:880px;height:63px;background:var(--footer);color:#ddd;font-size:9.5px}
.footer .legal{position:absolute;left:72px;top:25px;display:flex;gap:14px}
.footer .links{position:absolute;left:478px;top:27px;display:flex;gap:10px;font-size:9px}
.footer .social{position:absolute;left:770px;top:22px;display:flex;gap:5px}
.footer .social span{width:17px;height:17px;border-radius:50%;background:#777;display:block}
</style>
</head>
<body>

<header>
  <div class="abs brand"><span class="brand-dot"></span><span class="brand-name">Verdant Row</span></div>
  <div class="abs topbar">
    <span>TOLL FREE &nbsp;800-555-0142</span><span>|</span><span>LANDLINE &nbsp;555-010-2233</span><span>|</span><span>LOGIN</span><span>|</span><span>GET REGISTERED</span>
  </div>
  <nav class="abs nav">
    <a class="active" href="#">Home</a><a href="#">About</a><a href="#">Services</a><a href="#">Estimate</a><a href="#">Contact Us</a>
  </nav>
</header>

<section>
  <div class="abs hero" role="img" aria-label="Photo of a sunny Florida garden with flower beds, green lawn and a house"></div>
  <div class="abs hero-arrow left"><svg width="10" height="14" viewBox="0 0 10 14"><path d="M8 1 2 7l6 6" fill="none" stroke="#e94a33" stroke-width="2.5"/></svg></div>
  <div class="abs hero-arrow right"><svg width="10" height="14" viewBox="0 0 10 14"><path d="M2 1l6 6-6 6" fill="none" stroke="#e94a33" stroke-width="2.5"/></svg></div>
  <div class="abs hero-band">
    <h1>WELCOME TO VERDANT ROW</h1>
    <p>"Your Year Around Lawn Care Solution"</p>
  </div>
  <svg class="abs notch" width="56" height="16" viewBox="0 0 56 16"><path d="M0 0h56L28 16z" fill="#e94a33"/><path d="M14 2l14 8 14-8" fill="none" stroke="#fff" stroke-width="2"/></svg>
</section>

<section>
  <h2 class="abs section-title" style="top:422px">WHO WE ARE</h2>
  <p class="abs lead">Verdant Row is SAFE, Reliable, and Responsible. We make sure that all of our lawn care professionals are licensed, insured, drug-free, background checks completed and legally eligible to work.</p>
  <p class="abs blurb">Verdant Row offers convenient online bill pay, we accepts credit cards, and we pride ourselves with a great customer service department.If you are tired of lawn service companies that deliver poor quality, never call you back, have lousy communication skills, and are generally unprofessional and unreliable please consider giving Verdant Row a try !</p>
</section>

<section>
  <h2 class="abs section-title" style="top:578px">OUR SERVICES</h2>

  <div class="abs service" style="left:62px;top:628px">
    <svg width="52" height="40" viewBox="0 0 52 40"><path d="M2 4h8l6 16h22l4-12H14" fill="none" stroke="#5fa22e" stroke-width="3"/><circle cx="28" cy="31" r="6" fill="none" stroke="#5fa22e" stroke-width="3"/></svg>
    <h3>Lawn Care</h3><p>Lorem ipsum dolor sit amet, consectetuer adipiscing elit, sed diam nonummy</p><span class="more">READMORE ›</span>
  </div>
  <div class="abs service" style="left:320px;top:628px">
    <svg width="40" height="40" viewBox="0 0 40 40"><path d="M20 10c-4-4-6-6-6-8 3 1 5 3 6 5 1-2 3-4 6-5 0 2-2 4-6 8z M20 14v20 M20 34c-8 0-12-6-12-12 6 0 12 4 12 12z M20 34c8 0 12-6 12-12-6 0-12 4-12 12z" fill="#5fa22e" stroke="#5fa22e" stroke-width="2"/></svg>
    <h3>Flower Bed Maintenance</h3><p>Lorem ipsum dolor sit amet, consectetuer adipiscing elit, sed diam nonummy</p><span class="more">READMORE ›</span>
  </div>
  <div class="abs service" style="left:578px;top:628px">
    <svg width="50" height="40" viewBox="0 0 50 40"><path d="M4 2l12 20" stroke="#5fa22e" stroke-width="3"/><rect x="12" y="20" width="24" height="10" rx="3" fill="#5fa22e"/><circle cx="16" cy="33" r="5" fill="#5fa22e"/><circle cx="36" cy="33" r="5" fill="none" stroke="#5fa22e" stroke-width="3"/></svg>
    <h3>Trimming and Pruning</h3><p>Lorem ipsum dolor sit amet, consectetuer adipiscing elit, sed diam nonummy</p><span class="more">READMORE ›</span>
  </div>

  <div class="abs service" style="left:62px;top:718px">
    <svg width="50" height="40" viewBox="0 0 50 40"><path d="M24 22c0-10 8-16 20-16-1 12-8 16-20 16z M24 22c-4-8-10-10-16-8 2 6 8 10 16 8z" fill="#5fa22e"/><path d="M2 30c10 0 14-4 22-4s10 4 18 2c-6 6-12 8-22 8H2z" fill="#5fa22e"/></svg>
    <h3>Plant and Shrub Installation</h3><p>Lorem ipsum dolor sit amet, consectetuer adipiscing elit, sed diam nonummy</p><span class="more">READMORE ›</span>
  </div>
  <div class="abs service" style="left:320px;top:718px">
    <svg width="46" height="50" viewBox="0 0 46 50"><path d="M36 6 14 30" stroke="#5fa22e" stroke-width="5"/><path d="M14 30l-6 6 4 12" fill="none" stroke="#5fa22e" stroke-width="4"/><circle cx="40" cy="4" r="1.5" fill="#5fa22e"/><circle cx="44" cy="8" r="1.5" fill="#5fa22e"/><circle cx="42" cy="1" r="1.2" fill="#5fa22e"/></svg>
    <h3>Power Washing</h3><p>Lorem ipsum dolor sit amet, consectetuer adipiscing elit, sed diam nonummy</p><span class="more">READMORE ›</span>
  </div>
  <div class="abs service" style="left:578px;top:718px">
    <svg width="50" height="48" viewBox="0 0 50 48"><circle cx="32" cy="12" r="10" fill="#5fa22e"/><path d="M32 20v12" stroke="#5fa22e" stroke-width="3"/><rect x="4" y="26" width="20" height="10" rx="2" fill="#5fa22e"/><circle cx="8" cy="40" r="5" fill="none" stroke="#5fa22e" stroke-width="3"/><circle cx="22" cy="40" r="5" fill="none" stroke="#5fa22e" stroke-width="3"/></svg>
    <h3>Tree Trimming/Removal</h3><p>Lorem ipsum dolor sit amet, consectetuer adipiscing elit, sed diam nonummy</p><span class="more">READMORE ›</span>
  </div>
</section>

<section class="abs newsletter">
  <svg class="abs" style="left:0;top:0" width="880" height="128" viewBox="0 0 880 128"><polygon points="0,18 880,0 880,110 0,128" fill="#d83a24"/><polygon points="0,20 880,8 880,104 0,116" fill="#ea4a33"/></svg>
  <h2>Sign up for a Newaletter &amp; Get Latest Updates from VERDANT ROW</h2>
  <div class="field" style="left:126px">Name</div>
  <div class="field" style="left:300px">Email</div>
  <div class="field" style="left:474px">Phone Number</div>
  <div class="send">SEND</div>
</section>

<div class="abs grass" role="img" aria-label="Strip of green grass along the bottom of the page"></div>
<div class="abs mascot" role="img" aria-label="Illustration of a red cartoon lawn mower mascot"></div>

<section class="info">
  <svg class="abs" style="left:62px;top:962px" width="44" height="58" viewBox="0 0 44 58"><path d="M22 2C11 2 2 11 2 22c0 14 20 34 20 34s20-20 20-34C42 11 33 2 22 2z" fill="#ea4a33"/><circle cx="22" cy="22" r="9" fill="#fff"/><circle cx="22" cy="22" r="4.5" fill="#ea4a33"/></svg>
  <div class="abs" style="left:127px;top:957px">
    <h4>WE SERVE</h4>
    <div class="sub" style="margin-top:4px">HARBOR GLEN<br>PALM CREST SHORES</div>
  </div>

  <svg class="abs" style="left:316px;top:964px" width="48" height="50" viewBox="0 0 48 50"><path d="M6 8c4-4 8-4 10 0l4 8c1 3-2 5-4 6 2 6 6 10 12 12 1-2 3-5 6-4l8 4c4 2 4 6 0 10-6 6-16 2-26-8S0 14 6 8z" fill="#ea4a33"/><path d="M28 14a8 8 0 0 1 8 8 M28 6a16 16 0 0 1 16 16" fill="none" stroke="#ea4a33" stroke-width="3"/></svg>
  <div class="abs" style="left:387px;top:957px">
    <h4>CALL NOW</h4>
    <div class="small" style="margin-top:5px;width:150px">For a refreshing lawn care experience</div>
    <div class="phone">800-555-YARD</div>
    <div class="small" style="letter-spacing:6px;margin-left:70px;font-size:8.5px">9273</div>
  </div>

  <svg class="abs" style="left:582px;top:962px" width="42" height="58" viewBox="0 0 42 58"><rect x="2" y="2" width="38" height="54" rx="3" fill="none" stroke="#ea4a33" stroke-width="3"/><text x="21" y="28" text-anchor="middle" font-family="Montserrat,sans-serif" font-weight="700" font-size="20" fill="#ea4a33">$</text><path d="M10 38h22M10 44h22M10 50h22" stroke="#ea4a33" stroke-width="2.5"/></svg>
  <div class="abs" style="left:643px;top:957px">
    <h4>REQUEST</h4>
    <div class="quote">FREE QUOTE</div>
    <div class="small" style="width:140px;font-size:9px;line-height:11px">Try us with no risk and zero commitment.</div>
  </div>
</section>

<footer class="abs footer">
  <div class="legal"><span>VERDANT ROW © 2014</span><span>|</span><span>Terms &amp; Services</span><span>|</span><span>Privacy Policy</span></div>
  <div class="links"><span>Home</span><span>|</span><span>About</span><span>|</span><span>Services</span><span>|</span><span>Estimate</span><span>|</span><span>Contact Us</span></div>
  <div class="social"><span></span><span></span><span></span></div>
</footer>

</body>
</html>
```